(new) Verdant Pathway Health Coaching business needs a WordPress theme/website!

Hi! I am launching my health coaching business (7mapleroots Nutrition Coaching) and am need of a site design that I can plug into WordPress. I've attached my logos, social media squares, and one program form template -- I would like the website to reflect and compliment this branding so far (working tagline of "Health is for every body"... though I am open to suggestions). If helpful, my personal IG is @tilvarenq as all photos there are my original work.

The site should include blog, about me, contact me, testimonials, and health history form templates that I can customize if needed. The overall look and feel should me minimalist yet warm and inviting. My offerings will enable the client to consider what truly nourishes their lives in addition to the food on their plate. Thanks in advance!

```html
<!DOCTYPE html>
<html lang="en">
<head>
<meta charset="utf-8">
<title>7mapleroots Nutrition Coaching</title>
<link href="https://fonts.googleapis.com/css2?family=Lato:wght@400;700;900&display=swap" rel="stylesheet">
<style>
:root{
  --blue:#0e4c88;
  --blue-dark:#0a3b6b;
  --blue-deep:#083260;
  --blue-bright:#1f78c8;
  --ink:#1c1c1c;
  --text:#555;
  --line:#e3e3e3;
  --white:#fff;
}
*{box-sizing:border-box;margin:0;padding:0}
html,body{width:1200px;height:5213px;overflow:hidden;background:var(--white)}
body{font-family:'Lato',sans-serif;color:var(--ink)}
.page{position:relative;width:1200px;height:5213px;overflow:hidden}
.abs{position:absolute}
.photo{position:absolute}
.btn{position:absolute;display:flex;align-items:center;justify-content:center;background:var(--blue);color:#fff;font-weight:700;font-size:14px;letter-spacing:.3px;border-radius:3px}

/* header */
.site-header{position:absolute;left:0;top:0;width:1200px;height:122px;background:#fff;z-index:5}
.brand{position:absolute;left:100px;top:14px;width:220px;height:100px;display:flex;flex-direction:column;align-items:center}
.brand-mark{width:62px;height:62px;border:3px solid var(--blue);border-radius:50%}
.brand-name{margin-top:8px;color:var(--blue);font-weight:700;font-size:16px;letter-spacing:2.5px}
.call{position:absolute;left:486px;top:18px;display:flex;align-items:center;gap:10px}
.call-icon{width:36px;height:36px;border-radius:50%;background:var(--blue);display:flex;align-items:center;justify-content:center}
.call small{display:block;font-size:13px;color:var(--blue);font-weight:700}
.call strong{display:block;font-size:19px;color:var(--blue);font-weight:900}
.form-btn{left:708px;top:16px;width:204px;height:43px;font-size:14px}
.socials{position:absolute;left:937px;top:16px;display:flex;gap:12px}
.socials span{width:42px;height:42px;border:2px solid var(--blue-dark);border-radius:50%}
.nav{position:absolute;left:411px;top:81px;display:flex;gap:23px;font-size:17px;font-weight:700;color:#222}
.nav .active{color:var(--blue-bright)}

/* hero */
.hero{position:absolute;left:0;top:122px;width:1200px;height:670px;background:linear-gradient(120deg,#6d7a3a 0%,#8c8a4f 35%,#b7a06c 60%,#7b8746 85%,#5d6e34 100%)}
.hero h1{position:absolute;left:142px;top:228px;color:#fff;font-size:50px;line-height:57px;font-weight:900;letter-spacing:-.5px}
.hero .btn{left:144px;top:364px;width:160px;height:44px}
.dots{position:absolute;left:142px;top:444px;display:flex;gap:5px}
.dots i{width:13px;height:13px;border:2px solid #fff;border-radius:50%}
.dots i.on{background:#fff}
.hero-wave{position:absolute;left:0;bottom:0}

/* about */
.about-photo{left:145px;top:882px;width:390px;height:390px;border-radius:50%;background:radial-gradient(circle at 40% 40%,#7e8a66,#3e4a35)}
.about h2{position:absolute;left:611px;top:878px;font-size:32px;font-weight:700}
.rule{position:absolute;height:3px;background:var(--blue)}
.about p{position:absolute;left:611px;top:966px;width:450px;font-size:15px;line-height:25.7px;color:var(--text)}
.about .btn{left:611px;top:1204px;width:140px;height:41px;font-size:14px}

/* coaching */
.coaching{position:absolute;left:0;top:1330px;width:1200px;height:780px;background:linear-gradient(180deg,#1a5a8f,#174f83 50%,#1b5d8c)}
.coaching h2{position:absolute;left:0;width:1200px;top:1458px;text-align:center;font-size:38px;font-weight:700;color:#fff}
.card{position:absolute;top:1646px;width:234px;height:307px;background:#fff;border-radius:10px;text-align:center}
.card-photo{position:absolute;top:-66px;left:21px;width:192px;height:192px;border-radius:50%;border:4px solid var(--blue);outline:4px solid #fff}
.card h3{position:absolute;top:147px;left:0;width:100%;font-size:13.5px;font-weight:700;letter-spacing:.3px}
.card p{position:absolute;top:175px;left:22px;width:190px;font-size:13px;line-height:20px;color:var(--text)}
.card a,.more{position:absolute;font-size:13px;font-weight:700;color:var(--blue);text-decoration:none;letter-spacing:.3px}
.card a{top:270px;left:0;width:100%}

/* blog */
.blog-title{position:absolute;left:0;width:1200px;top:2164px;text-align:center;font-size:36px;font-weight:700}
.post{position:absolute;top:2287px;width:287px;height:476px;border:2px solid var(--line);background:#fff}
.post.raised{box-shadow:0 4px 14px rgba(120,60,140,.18)}
.post-photo{left:4px;top:4px;width:275px;height:225px}
.post .date{position:absolute;left:22px;top:251px;font-size:13px;color:#4aa6c8;letter-spacing:.3px}
.post h3{position:absolute;left:22px;top:284px;width:240px;font-size:13.5px;line-height:23px;font-weight:700}
.post p{position:absolute;left:22px;top:336px;width:245px;font-size:13px;line-height:21px;color:var(--text)}
.post .pill{position:absolute;left:22px;top:415px;width:125px;height:35px;border:2px solid #222;border-radius:18px;font-size:12px;font-weight:700;display:flex;align-items:center;justify-content:center;letter-spacing:.4px}

/* testimonials */
.testi-panel{position:absolute;left:0;top:2894px;width:662px;height:622px;background:var(--blue)}
.testi-photo{left:662px;top:2870px;width:538px;height:621px;background:linear-gradient(100deg,#2f8ad0,#3aa0d8 40%,#c49c7a 70%,#6c5a4c)}
.testi-panel h2{position:absolute;left:146px;top:66px;font-size:38px;font-weight:700;color:#fff}
.quote{position:absolute;left:146px;width:450px}
.quote .mark{position:absolute;left:-4px;top:-18px;font-size:90px;line-height:90px;color:#8ea8c6;font-weight:900}
.quote p{position:absolute;left:56px;top:0;width:390px;font-size:14.5px;line-height:22.7px;color:#fff}
.quote .who{position:absolute;left:52px;top:112px;display:flex;gap:16px;color:#fff}
.avatar{width:81px;height:81px;border-radius:50%;border:3px solid #fff;background:linear-gradient(135deg,#c89a78,#58707e)}
.who b{display:block;font-size:15px;font-weight:400;line-height:22px}
.who .stars{font-size:15px;letter-spacing:2px}

/* contact */
.contact-photo{left:142px;top:3627px;width:635px;height:654px;border-radius:0 0 40px 0;background:linear-gradient(160deg,#6f9a52,#4a7a3a 40%,#9aa690 70%,#b9b6ad)}
.contact-box{position:absolute;left:561px;top:3692px;width:494px;height:518px;background:var(--blue);border-radius:40px 40px 40px 0}
.contact-box::before{content:"";position:absolute;left:-9px;top:-9px;right:-9px;bottom:-9px;border:2px solid #fff;border-radius:46px 46px 46px 0;z-index:-1}
.contact-box h2{position:absolute;left:54px;top:38px;font-size:38px;font-weight:700;color:#fff}
.field{position:absolute;left:56px;width:393px;height:37px;border:1.5px solid #fff;border-radius:3px;color:#fff;font-size:11.5px;padding:11px 16px}
.submit{position:absolute;left:56px;top:433px;width:150px;height:45px;background:#fff;color:var(--blue);font-weight:900;font-size:16px;display:flex;align-items:center;justify-content:center;border-radius:3px}

/* instagram */
.insta{position:absolute;top:4406px;height:320px;width:300px}
.insta-label{position:absolute;left:0;width:1200px;top:4521px;text-align:center;color:#fff;font-weight:900;font-size:17px;letter-spacing:.5px}
.insta-icon{position:absolute;left:738px;top:4474px}

/* footer */
.site-footer{position:absolute;left:0;top:4726px;width:1200px;height:395px;background:var(--blue)}
.foot-brand{position:absolute;left:163px;top:88px;width:136px;height:136px;border:4px solid #fff;border-radius:50%;display:flex;align-items:center;justify-content:center;color:#fff;font-weight:700;font-size:13px;text-align:center;letter-spacing:1px;line-height:18px}
.foot-social{position:absolute;left:168px;top:252px;display:flex;gap:4px}
.foot-social span{width:28px;height:28px;border:1.5px solid #fff;border-radius:50%}
.site-footer h4{position:absolute;font-size:17px;font-weight:900;color:#fff;letter-spacing:.2px}
.foot-item{position:absolute;left:356px;display:flex;gap:16px;color:#fff;font-size:13.5px;line-height:21px}
.foot-item svg{flex:none;margin-top:2px}
.signup-text{position:absolute;left:585px;top:104px;width:310px;color:#fff;font-size:13px;line-height:22px}
.email-input{position:absolute;left:585px;top:172px;width:303px;height:37px;background:#fff;border-radius:2px;font-size:13px;color:#555;padding:10px 16px}
.subscribe{position:absolute;left:585px;top:227px;width:119px;height:38px;background:var(--blue-deep);color:#fff;font-size:12.5px;font-weight:700;display:flex;align-items:center;justify-content:center;border-radius:2px}
.quick{position:absolute;left:940px;top:106px;list-style:none;color:#fff;font-size:13.5px;line-height:30px}
.copyright{position:absolute;left:0;top:5121px;width:1200px;height:92px;background:var(--blue-dark);color:#fff;font-size:13px;display:flex;align-items:center;justify-content:center}
</style>
</head>
<body>
<div class="page">

<header class="site-header">
  <div class="brand">
    <div class="brand-mark"></div>
    <div class="brand-name">7MAPLEROOTS</div>
  </div>
  <div class="call">
    <div class="call-icon"><svg width="18" height="18" viewBox="0 0 24 24" fill="#fff"><path d="M6.6 10.8a15 15 0 0 0 6.6 6.6l2.2-2.2c.3-.3.7-.4 1-.2 1.1.4 2.3.6 3.6.6.6 0 1 .4 1 1V20c0 .6-.4 1-1 1A17 17 0 0 1 3 4c0-.6.4-1 1-1h3.5c.6 0 1 .4 1 1 0 1.3.2 2.5.6 3.6.1.3 0 .7-.2 1z"/></svg></div>
    <div><small>Call Us :</small><strong>808 3300 5500</strong></div>
  </div>
  <div class="btn form-btn">FORM DOWNLOAD</div>
  <div class="socials"><span></span><span></span><span></span></div>
  <nav class="nav"><span class="active">Home</span><span>About Me</span><span>Services</span><span>Blog</span><span>Testimonials</span><span>Health History</span><span>Contact Me</span></nav>
</header>

<section class="hero" role="img" aria-label="Woman skipping rope outdoors in a sunny park">
  <h1>HEALTH IS FOR<br>EVERYBODY</h1>
  <div class="btn">LEARN MORE</div>
  <div class="dots"><i class="on"></i><i></i><i></i><i></i></div>
  <svg class="hero-wave" width="1200" height="110" viewBox="0 0 1200 110">
    <path d="M0 110 L0 80 C150 45 300 30 480 40 C700 52 900 80 1050 55 C1120 42 1170 25 1200 10 L1200 110 Z" fill="#0e4c88"/>
    <path d="M0 110 L0 94 C150 60 300 45 480 55 C700 67 900 96 1050 72 C1120 60 1170 46 1200 34 L1200 110 Z" fill="#fff"/>
  </svg>
</section>

<section class="about">
  <div class="photo about-photo" role="img" aria-label="Coach leaning on a tree in a park"></div>
  <h2>About Me</h2>
  <div class="rule" style="left:611px;top:930px;width:68px"></div>
  <p>Sed ut perspiciatis unde omnis iste natus error sit voluptatem accusantium doloremque laudantium, totam rem aperiam, eaque ipsa quae ab illo inventore veritatis et quasi architecto beatae vitae dicta sunt explicabo. Nemo enim ipsam voluptatem quia voluptas sit aspernatur aut odit aut fugit, sed quia consequuntur magni dolores eos qui ratione voluptatem sequi nesciunt. Neque porro quisquam est, qui dolorem ipsum quia dolor sit amet, consectetur, adipisci velit</p>
  <div class="btn">READ MORE</div>
</section>

<section class="coaching" role="img" aria-label="Blue-tinted background of trees in a park"></section>
<svg class="abs" style="left:0;top:1320px" width="1200" height="80" viewBox="0 0 1200 80"><path d="M0 0 H1200 V30 C1050 10 900 60 700 55 C500 50 350 0 200 10 C120 15 50 40 0 60 Z" fill="#fff"/></svg>
<svg class="abs" style="left:0;top:2030px" width="1200" height="82" viewBox="0 0 1200 82"><path d="M0 82 H1200 V50 C1100 20 950 40 800 50 C600 62 420 10 250 20 C150 26 70 50 0 55 Z" fill="#fff"/></svg>
<h2 class="coaching" style="background:none;height:auto;top:1458px"><span style="display:block;width:1200px;text-align:center;font-size:38px;color:#fff">7mapleroots Nutrition Coaching</span></h2>
<div class="rule" style="left:569px;top:1520px;width:62px;background:#fff"></div>

<div class="card" style="left:111px"><div class="card-photo" role="img" aria-label="Woman measuring her waist in a kitchen" style="background:linear-gradient(135deg,#7a5a40,#c9a27e)"></div><h3>NEMO ENIM IPSAM</h3><p>Sed ut perspiciatis unde omnis iste natus error sit voluptatem acantium dremque laudantium, totam rem aperiam</p><a>LEARN MORE &nbsp;→</a></div>
<div class="card" style="left:359px"><div class="card-photo" role="img" aria-label="Trainer coaching a client at the gym" style="background:linear-gradient(135deg,#3a3a3a,#b99a84)"></div><h3>NEMO ENIM IPSAM</h3><p>Sed ut perspiciatis unde omnis iste natus error sit voluptatem acantium dremque laudantium, totam rem aperiam</p><a>LEARN MORE &nbsp;→</a></div>
<div class="card" style="left:607px"><div class="card-photo" role="img" aria-label="Two people drinking water after a run" style="background:linear-gradient(135deg,#6d9a4e,#d9c1a8)"></div><h3>NEMO ENIM IPSAM</h3><p>Sed ut perspiciatis unde omnis iste natus error sit voluptatem acantium dremque laudantium, totam rem aperiam</p><a>LEARN MORE &nbsp;→</a></div>
<div class="card" style="left:855px"><div class="card-photo" role="img" aria-label="Woman with a measuring tape around her body" style="background:linear-gradient(135deg,#e9f1f6,#c8a792)"></div><h3>NEMO ENIM IPSAM</h3><p>Sed ut perspiciatis unde omnis iste natus error sit voluptatem acantium dremque laudantium, totam rem aperiam</p><a>LEARN MORE &nbsp;→</a></div>

<h2 class="blog-title">Latest Blog</h2>
<div class="rule" style="left:563px;top:2229px;width:74px"></div>

<article class="post" style="left:142px"><div class="photo post-photo" role="img" aria-label="Woman on an indoor climbing wall" style="background:linear-gradient(120deg,#8a6a4e,#c7b39a 60%,#3d3a38)"></div><div class="date">▦ FEB 13, 2020</div><h3>NEMO ENIM IPSAM VOLUP QUIA VOLUPTAS SIT</h3><p>Sed ut perspiciatis unde omnis iste natus error sit voluptatem acsntium domque laudantium, totam</p><div class="pill">LEARN MORE</div></article>
<article class="post raised" style="left:455px"><div class="photo post-photo" role="img" aria-label="Runner checking a fitness watch" style="background:linear-gradient(120deg,#b3302d,#6e8a45 60%,#c9d4b0)"></div><div class="date">▦ FEB 13, 2020</div><h3>NEMO ENIM IPSAM VOLUP QUIA VOLUPTAS SIT</h3><p>Sed ut perspiciatis unde omnis iste natus error sit voluptatem acsntium domque laudantium, totam</p><div class="pill">LEARN MORE</div></article>
<article class="post" style="left:769px"><div class="photo post-photo" role="img" aria-label="Grilled chicken on a fresh salad" style="background:linear-gradient(120deg,#9a5a2a,#5e8a3a 55%,#c0862e)"></div><div class="date">▦ FEB 13, 2020</div><h3>NEMO ENIM IPSAM VOLUP QUIA VOLUPTAS SIT</h3><p>Sed ut perspiciatis unde omnis iste natus error sit voluptatem acsntium domque laudantium, totam</p><div class="pill">LEARN MORE</div></article>

<div class="photo testi-photo" role="img" aria-label="Smiling woman measuring her waist in a bright kitchen"></div>
<section class="testi-panel">
  <h2>Testimonials</h2>
  <div class="rule" style="left:393px;top:92px;width:56px;background:#fff"></div>
  <svg class="abs" style="left:578px;top:80px" width="44" height="26" viewBox="0 0 44 26" fill="none" stroke="#fff" stroke-width="3"><path d="M12 3 3 13l9 10M32 3l9 10-9 10"/></svg>
  <div class="quote" style="top:142px"><span class="mark">“</span><p>Nemo enim ipsam voluptatem quia voluptas sit aspernatur aut odit aut fugit, sed quia consequuntur magni dolores eos qui ratione voluptatem sequi nesciunt. Neque porro quisquam est</p><div class="who"><div class="avatar" role="img" aria-label="Client portrait"></div><div style="padding-top:12px"><b>John Doe</b><b>Nutrition Coaching</b><span class="stars">★★★★★</span></div></div></div>
  <div class="quote" style="top:358px"><span class="mark">“</span><p>Nemo enim ipsam voluptatem quia voluptas sit aspernatur aut odit aut fugit, sed quia consequuntur magni dolores eos qui ratione voluptatem sequi nesciunt. Neque porro quisquam est</p><div class="who"><div class="avatar" role="img" aria-label="Client portrait"></div><div style="padding-top:12px"><b>John Doe</b><b>Nutrition Coaching</b><span class="stars">★★★★★</span></div></div></div>
</section>

<div class="photo contact-photo" role="img" aria-label="Woman in a green jacket stretching before a run"></div>
<section class="contact-box" style="z-index:1">
  <h2>Contact Me</h2>
  <div class="rule" style="left:56px;top:98px;width:70px;background:#fff"></div>
  <div class="field" style="top:137px">First Name *</div>
  <div class="field" style="top:186px">Last Name *</div>
  <div class="field" style="top:236px">Phone *</div>
  <div class="field" style="top:287px">E-mail Address</div>
  <div class="field" style="top:336px;height:81px">Message</div>
  <div class="submit">SUBMIT</div>
</section>

<div class="insta" role="img" aria-label="Climber on a bouldering wall" style="left:0;background:linear-gradient(135deg,#8c8c86,#5d5a56)"></div>
<div class="insta" role="img" aria-label="Chocolate cake slice" style="left:300px;background:linear-gradient(135deg,#3a2418,#7a5a44)"></div>
<div class="insta" role="img" aria-label="Colourful vegetable salad" style="left:600px;background:linear-gradient(135deg,#5b8a2e,#a83a2a)"></div>
<div class="insta" role="img" aria-label="Friends in costumes at a party" style="left:900px;background:linear-gradient(135deg,#7a6a5a,#b08c3a)"></div>
<svg class="insta-icon" width="26" height="26" viewBox="0 0 26 26" fill="none" stroke="#fff" stroke-width="2.2"><rect x="2" y="2" width="22" height="22" rx="6"/><circle cx="13" cy="13" r="5"/></svg>
<div class="insta-label">OUR INSTAGRAM</div>

<footer class="site-footer">
  <div class="foot-brand">7MAPLE<br>ROOTS</div>
  <div class="foot-social"><span></span><span></span><span></span><span></span></div>
  <h4 style="left:356px;top:60px">CONTACT US</h4>
  <div class="foot-item" style="top:100px"><svg width="16" height="20" viewBox="0 0 16 20" fill="none" stroke="#fff" stroke-width="1.6"><path d="M8 19s6-6.5 6-11A6 6 0 0 0 2 8c0 4.5 6 11 6 11z"/><circle cx="8" cy="8" r="2.2"/></svg><span>7mapleroots Nutrition<br>Coaching. PO Box 41<br>Larkfield, MA 02190</span></div>
  <div class="foot-item" style="top:174px"><svg width="16" height="16" viewBox="0 0 24 24" fill="none" stroke="#fff" stroke-width="1.8"><path d="M6.6 10.8a15 15 0 0 0 6.6 6.6l2.2-2.2c.3-.3.7-.4 1-.2 1.1.4 2.3.6 3.6.6.6 0 1 .4 1 1V20c0 .6-.4 1-1 1A17 17 0 0 1 3 4c0-.6.4-1 1-1h3.5c.6 0 1 .4 1 1 0 1.3.2 2.5.6 3.6.1.3 0 .7-.2 1z"/></svg><span>Phone :<br>781-555-0162</span></div>
  <div class="foot-item" style="top:236px"><svg width="18" height="14" viewBox="0 0 18 14" fill="none" stroke="#fff" stroke-width="1.5"><rect x="1" y="1" width="16" height="12"/><path d="m1 1 8 7 8-7"/></svg><span>Email :<br>info@7mapleroots.com</span></div>
  <h4 style="left:585px;top:58px">SIGN UP TO RECEIVE EMAIL</h4>
  <p class="signup-text">Excepteur sint occaecat cupidatat non proident, sunt in culpa qui Nemo enim ipsam voluptatem</p>
  <div class="email-input">Enter Email</div>
  <div class="subscribe">SUBSCRIBE</div>
  <h4 style="left:935px;top:58px">QUICK LINKS</h4>
  <ul class="quick"><li>Home</li><li>About Me</li><li>Our Services</li><li>Blog</li><li>Contact Me</li><li>Testimonials</li></ul>
</footer>
<div class="copyright">Copyright © 7mapleroots Nutrition Coaching 2020. All rights reserved. | Privacy Policy</div>

</div>
</body>
</html>
```